New Company Business Card Design

I have a new company logo and I want a new business card design. I dont know if the logo file i attached is in the correct format or quality. We are a New York City Specialty construction Firm specializing in high risk out of the box projects. I want a simple and classy business card that people will his card is as crisp as the work his company does.

Target Market(s)

Clients in the heavy construction industry in New York City

Industry/Entity Type

Construction Company

Contact Information for Business Card

Simple Classy - DIFFERENT

Font styles to use
Other font styles liked:
• Mach the logo font in some way

Colors

Designer to choose colors to be used in the design.

Requirements
Must have
• Uniqueness
Nice to have
• Nothing particular - Just different and classy - Timeless
Should not have
• Goofy Shit or Gimmicky shit

```html
<!DOCTYPE html>
<html lang="en">
<head>
<meta charset="utf-8">
<title>KVR Associates – Business Card</title>
<link rel="stylesheet" href="https://fonts.googleapis.com/css2?family=Arimo:wght@400;700&display=swap">
<style>
  :root {
    --backdrop: #d9dadb;
    --card: #f7f7f5;
    --ink: #1c1c1c;
    --brand-blue: #1f74c4;
    --rule-blue: #3a8fd6;
    --muted: #333333;
  }
  * { box-sizing: border-box; margin: 0; padding: 0; }
  html, body {
    width: 1200px; height: 1200px; overflow: hidden;
    background: var(--backdrop);
    font-family: "Arimo", Arial, sans-serif;
    color: var(--ink);
  }
  .sheet {
    width: 1200px; height: 1200px;
    display: flex; flex-direction: column; align-items: center; justify-content: center;
    gap: 60px;
  }
  .card {
    position: relative;
    width: 840px; height: 480px;
    background: var(--card);
    box-shadow: 0 3px 10px rgba(0,0,0,.18);
  }

  /* ---------- contact side ---------- */
  .brand {
    display: flex; align-items: center; gap: 14px;
    font-weight: 700; color: var(--brand-blue);
  }
  .brand-square { background: var(--brand-blue); flex: none; }
  .card-front .brand { position: absolute; left: 150px; top: 58px; font-size: 40px; }
  .card-front .brand-square { width: 30px; height: 30px; }
  .front-rule {
    position: absolute; left: 110px; right: 60px; top: 178px;
    height: 4px; background: var(--brand-blue);
  }
  .person {
    position: absolute; right: 80px; top: 110px; text-align: center;
    color: var(--brand-blue);
  }
  .person-name { font-weight: 700; font-size: 24px; }
  .person-title { font-size: 22px; margin-top: 2px; }
  .address {
    position: absolute; left: 90px; top: 205px;
    font-weight: 700; font-size: 24px; line-height: 1.3; font-style: normal;
  }
  .contacts {
    position: absolute; left: 440px; top: 280px;
    font-size: 23px; line-height: 1.45;
    display: grid; grid-template-columns: 92px 20px auto;
  }
  .contacts dt { color: var(--muted); }
  .contacts .sep { font-weight: 700; }
  .contacts dd { font-weight: 700; }

  /* ---------- reverse side ---------- */
  .card-back .brand {
    position: absolute; left: 0; right: 0; top: 110px;
    justify-content: center; font-size: 64px;
  }
  .card-back .brand-square { width: 46px; height: 46px; }
  .back-rule {
    position: absolute; left: 90px; right: 90px; top: 262px;
    height: 3px; background: var(--rule-blue);
  }
  .web {
    position: absolute; left: 0; right: 0; top: 320px; text-align: center;
    font-weight: 700; font-size: 46px; letter-spacing: 6px;
  }
</style>
</head>
<body>
<main class="sheet">

  <section class="card card-front" aria-label="Business card, contact side">
    <div class="brand"><span class="brand-square"></span><span class="brand-name">KVR Associates, Inc.</span></div>
    <div class="person">
      <p class="person-name">Marco T. Renaldi</p>
      <p class="person-title">CEO</p>
    </div>
    <div class="front-rule"></div>
    <address class="address">
      215<br>
      Harbor Line Street<br>
      Linden,<br>
      New Jersey 07036
    </address>
    <dl class="contacts">
      <dt>Phone</dt><span class="sep">:</span><dd>908-555-0142</dd>
      <dt>Cell</dt><span class="sep">:</span><dd>917-555-0187</dd>
      <dt>E-mail</dt><span class="sep">:</span><dd>marco@kvrbuild.com</dd>
    </dl>
  </section>

  <section class="card card-back" aria-label="Business card, reverse side">
    <div class="brand"><span class="brand-square"></span><span class="brand-name">KVR Associates, Inc.</span></div>
    <div class="back-rule"></div>
    <p class="web">WWW.KVRBUILD.COM</p>
  </section>

</main>
</body>
</html>
```